Used Car Dealer seeks an Amazing Business Card Design

We are looking for a business card design that incorporates our logo and grabs the attention of anyone we give the business card to.

Looking to use the same colors as the logo. Our Logo choice is the black background with Red and Silver/Grey Lettering.

We also would like to see some embossed designs.

Target Market(s)

Used Car Buyers, Automotive, Auto

Industry/Entity Type

Automotive

Contact Information for Business Card

BVEX7K
Gordon Whitley
482 Tenbrook Lane
Suite 305
Roswell, GA 30098
Office (770) 555-0142
Cell (770) 555-0187
bvex7kga@mailnest.example
www.bvex7kga.example

Colors
ffffff
ee3036

Requirements
Must have
• Must include our logo (Black Background with Red and Silver/Grey Lettering)
Nice to have
• Embossed Design. Can be Single or Double Sided.

```html
<!DOCTYPE html>
<html lang="en">
<head>
<meta charset="utf-8">
<title>BVEX7K Business Card</title>
<link href="https://fonts.googleapis.com/css2?family=Open+Sans:wght@400;600;700&display=swap" rel="stylesheet">
<style>
  :root {
    --bg: #e4e5e7;
    --card-black: #0b0b0c;
    --brand-red: #ee3036;
    --deep-red: #c8191f;
    --silver: #c9cacc;
    --white: #ffffff;
    --shadow: rgba(0,0,0,0.28);
  }
  html, body {
    margin: 0;
    padding: 0;
    width: 1200px;
    height: 1000px;
    overflow: hidden;
    background: var(--bg);
    font-family: "Open Sans", Arial, sans-serif;
  }
  .canvas {
    position: relative;
    width: 1200px;
    height: 1000px;
  }
  .card {
    position: absolute;
    left: 250px;
    width: 700px;
    height: 400px;
    border-radius: 30px;
    overflow: hidden;
    background: var(--card-black);
    box-shadow: 0 14px 30px var(--shadow);
  }
  .card--front { top: 70px; }
  .card--back { top: 530px; }
  .card__shapes {
    position: absolute;
    inset: 0;
    width: 100%;
    height: 100%;
  }
  .brand {
    position: absolute;
    display: flex;
    align-items: center;
    gap: 14px;
    color: var(--silver);
    font-weight: 700;
    font-size: 54px;
    letter-spacing: 2px;
  }
  .brand__dot {
    width: 22px;
    height: 22px;
    border-radius: 50%;
    background: var(--brand-red);
  }
  .card--front .brand { left: 90px; top: 160px; }
  .card--back .brand { left: 390px; top: 130px; font-size: 50px; }
  .contact {
    position: absolute;
    left: 58px;
    top: 48px;
    color: var(--white);
    font-size: 15px;
    line-height: 20px;
  }
  .contact__row {
    display: flex;
    align-items: flex-start;
    gap: 16px;
    margin-bottom: 14px;
  }
  .contact__icon {
    width: 18px;
    height: 18px;
    flex: none;
    margin-top: 2px;
  }
  .name-bar {
    position: absolute;
    left: 0;
    top: 258px;
    width: 300px;
    height: 54px;
    background: var(--deep-red);
    box-shadow: 0 6px 12px rgba(0,0,0,0.2);
    display: flex;
    align-items: center;
    padding-left: 50px;
    color: var(--white);
    font-weight: 600;
    font-size: 21px;
    letter-spacing: 1px;
    text-transform: uppercase;
  }
</style>
</head>
<body>
<main class="canvas">

  <section class="card card--front" aria-label="Card front">
    <svg class="card__shapes" viewBox="0 0 700 400" preserveAspectRatio="none">
      <polygon points="450,0 700,0 700,400 570,400 585,175" fill="var(--brand-red)"/>
      <polyline points="450,0 585,175 570,400" fill="none" stroke="#5a0c0f" stroke-width="4"/>
    </svg>
    <div class="brand"><span class="brand__dot"></span>BVEX7K</div>
  </section>

  <section class="card card--back" aria-label="Card back">
    <svg class="card__shapes" viewBox="0 0 700 400" preserveAspectRatio="none">
      <polygon points="0,0 310,0 300,230 395,400 0,400" fill="var(--brand-red)"/>
      <polyline points="310,0 300,230 395,400" fill="none" stroke="#5a0c0f" stroke-width="4"/>
    </svg>

    <div class="contact">
      <div class="contact__row">
        <svg class="contact__icon" viewBox="0 0 24 24"><path fill="var(--white)" d="M6.6 10.8a15 15 0 0 0 6.6 6.6l2.2-2.2a1 1 0 0 1 1-.25 11.4 11.4 0 0 0 3.6.57 1 1 0 0 1 1 1V20a1 1 0 0 1-1 1A17 17 0 0 1 3 4a1 1 0 0 1 1-1h3.5a1 1 0 0 1 1 1c0 1.25.2 2.45.57 3.57a1 1 0 0 1-.25 1z"/></svg>
        <div>(770) 555-0142<br>(770) 555-0187</div>
      </div>
      <div class="contact__row">
        <svg class="contact__icon" viewBox="0 0 24 24" fill="none" stroke="var(--white)" stroke-width="1.8"><circle cx="12" cy="12" r="9.5"/><ellipse cx="12" cy="12" rx="4" ry="9.5"/><line x1="2.5" y1="12" x2="21.5" y2="12"/></svg>
        <div>bvex7kga@mailnest.example<br>www.bvex7kga.example</div>
      </div>
      <div class="contact__row">
        <svg class="contact__icon" viewBox="0 0 24 24"><path fill="var(--white)" d="M12 2a7 7 0 0 0-7 7c0 5.25 7 13 7 13s7-7.75 7-13a7 7 0 0 0-7-7zm0 9.5A2.5 2.5 0 1 1 12 6.5a2.5 2.5 0 0 1 0 5z"/></svg>
        <div>482 Tenbrook Lane<br>Suite 305<br>Roswell, GA 30098</div>
      </div>
    </div>

    <div class="name-bar">Gordon Whitley</div>

    <div class="brand"><span class="brand__dot"></span>BVEX7K</div>
  </section>

</main>
</body>
</html>
```